Clean Stationary Design For Print Shop

I need a clean stationary set that properly represents a local print and copy shop to make it look amazing. It should do the following:
- Compliment the color scheme of the logo.
- Be clean and sharp.
- Be colorful but but balanced.

This is what I need designed:
- Business Card
- Letter Head
- Envelop

Target Market(s)

Local customers and businesses, including hospitals and schools.

Industry/Entity Type

Digital Printing

Requirements
Must have
• Clean business card with logo on front and full color back with faded logo on it and social icons with @tollworthmarks beside each one (Pagelark & Glimmora).

```html
<!DOCTYPE html>
<html lang="en">
<head>
<meta charset="utf-8">
<title>Tollworth Marks Stationery Set</title>
<link rel="stylesheet" href="https://fonts.googleapis.com/css2?family=Montserrat+Alternates:wght@400;500&family=Open+Sans:wght@400&display=swap">
<style>
  :root {
    --backdrop: #a7a8ac;
    --ink: #07080a;
    --paper: #ffffff;
    --accent: #ee344c;
    --text-font: "Montserrat Alternates", sans-serif;
    --name-font: "Open Sans", sans-serif;
  }
  * { margin: 0; padding: 0; box-sizing: border-box; }
  html, body { width: 1200px; height: 986px; overflow: hidden; background: var(--backdrop); }
  .canvas { position: relative; width: 1200px; height: 986px; }

  .brand { display: flex; align-items: center; color: var(--paper); }
  .brand-square { background: var(--paper); flex: none; }
  .brand-name { font-family: var(--text-font); font-weight: 500; line-height: 1; white-space: nowrap; color: var(--paper); }

  .letterhead { position: absolute; left: 202px; top: 119px; width: 545px; height: 769px; background: var(--paper); }
  .letterhead .header { height: 86px; background: var(--ink); display: flex; justify-content: center; align-items: center; }
  .letterhead .brand-square { width: 30px; height: 30px; margin-right: 12px; }
  .letterhead .brand-name { font-size: 23px; }

  .contact-band { position: absolute; left: 0; bottom: 0; width: 100%; height: 63px; display: flex; }
  .contact-band .details { background: var(--ink); display: flex; align-items: center; justify-content: space-around; padding: 0 6px; }
  .contact-band .socials { background: var(--accent); flex: 1; display: flex; align-items: center; justify-content: space-around; padding: 0 4px; }
  .contact-item { display: flex; align-items: center; gap: 4px; color: var(--paper); font-family: var(--text-font); font-size: 7.4px; white-space: nowrap; }
  .contact-item svg { width: 14px; height: 14px; flex: none; }
  .letterhead .details { width: 358px; }

  .envelope { position: absolute; left: 529px; top: 336px; width: 592px; height: 360px; background: var(--paper); border-radius: 45px 45px 0 0; overflow: hidden; }
  .envelope .header { height: 97px; background: var(--ink); display: flex; justify-content: center; align-items: center; padding-left: 20px; }
  .envelope .brand-square { width: 42px; height: 42px; margin-right: 16px; }
  .envelope .brand-name { font-size: 33px; }
  .envelope .details { width: 394px; }
  .envelope .contact-item { font-size: 7.6px; }

  .card { position: absolute; width: 231px; height: 132px; background: var(--ink); overflow: hidden; }
  .card .chevron { position: absolute; left: 0; top: 0; width: 100%; height: 100%; }
  .card-front { left: 133px; top: 362px; }
  .card-front .brand { position: absolute; left: 87px; top: 58px; }
  .card-front .brand-square { width: 15px; height: 15px; margin-right: 6px; }
  .card-front .brand-name { font-size: 12.5px; }

  .card-back { left: 136px; top: 508px; }
  .card-back .holder { position: absolute; left: 119px; top: 21px; color: var(--paper); }
  .holder-name { font-family: var(--name-font); font-weight: 400; font-size: 8px; letter-spacing: -0.1px; }
  .holder-role { font-family: var(--name-font); font-size: 4.6px; margin-top: 1px; }
  .holder-list { list-style: none; margin-top: 7px; }
  .holder-list .contact-item { font-size: 4.2px; gap: 3px; margin-bottom: 4px; }
  .holder-list .contact-item svg { width: 9px; height: 9px; }
</style>
</head>
<body>
<div class="canvas">

  <section class="letterhead">
    <header class="header">
      <div class="brand">
        <span class="brand-square"></span>
        <span class="brand-name">Tollworth Marks</span>
      </div>
    </header>
    <footer class="contact-band">
      <div class="details">
        <span class="contact-item"><svg viewBox="0 0 20 20"><circle cx="10" cy="10" r="9" fill="none" stroke="#ee344c" stroke-width="1.2"/><path d="M10 5a3 3 0 0 0-3 3c0 2.5 3 5 3 5s3-2.5 3-5a3 3 0 0 0-3-3z" fill="none" stroke="#fff" stroke-width="1"/></svg>Lorem ipsum dolor mirid proud</span>
        <span class="contact-item"><svg viewBox="0 0 20 20"><circle cx="10" cy="10" r="9" fill="none" stroke="#ee344c" stroke-width="1.2"/><path d="M6.5 6.5l2-1 1.2 2.2-1 .9a6 6 0 0 0 2.7 2.7l.9-1 2.2 1.2-1 2C9 13.5 6.5 11 6.5 6.5z" fill="none" stroke="#fff" stroke-width="1"/></svg>00 000 0000</span>
        <span class="contact-item"><svg viewBox="0 0 20 20"><circle cx="10" cy="10" r="9" fill="none" stroke="#ee344c" stroke-width="1.2"/><rect x="5.5" y="7" width="9" height="6.5" fill="none" stroke="#fff" stroke-width="1"/><path d="M5.5 7l4.5 3.5L14.5 7" fill="none" stroke="#fff" stroke-width="1"/></svg>info@tollworthmarks.com</span>
      </div>
      <div class="socials">
        <span class="contact-item"><svg viewBox="0 0 20 20"><circle cx="10" cy="10" r="9" fill="none" stroke="#07080a" stroke-width="1.2"/></svg>@tollworthmarks</span>
        <span class="contact-item"><svg viewBox="0 0 20 20"><circle cx="10" cy="10" r="9" fill="none" stroke="#07080a" stroke-width="1.2"/></svg>@tollworthmarks</span>
      </div>
    </footer>
  </section>

  <section class="envelope">
    <header class="header">
      <div class="brand">
        <span class="brand-square"></span>
        <span class="brand-name">Tollworth Marks</span>
      </div>
    </header>
    <footer class="contact-band">
      <div class="details">
        <span class="contact-item"><svg viewBox="0 0 20 20"><circle cx="10" cy="10" r="9" fill="none" stroke="#ee344c" stroke-width="1.2"/><path d="M10 5a3 3 0 0 0-3 3c0 2.5 3 5 3 5s3-2.5 3-5a3 3 0 0 0-3-3z" fill="none" stroke="#fff" stroke-width="1"/></svg>Lorem ipsum dolor mirid proud</span>
        <span class="contact-item"><svg viewBox="0 0 20 20"><circle cx="10" cy="10" r="9" fill="none" stroke="#ee344c" stroke-width="1.2"/><path d="M6.5 6.5l2-1 1.2 2.2-1 .9a6 6 0 0 0 2.7 2.7l.9-1 2.2 1.2-1 2C9 13.5 6.5 11 6.5 6.5z" fill="none" stroke="#fff" stroke-width="1"/></svg>00 000 0000</span>
        <span class="contact-item"><svg viewBox="0 0 20 20"><circle cx="10" cy="10" r="9" fill="none" stroke="#ee344c" stroke-width="1.2"/><rect x="5.5" y="7" width="9" height="6.5" fill="none" stroke="#fff" stroke-width="1"/><path d="M5.5 7l4.5 3.5L14.5 7" fill="none" stroke="#fff" stroke-width="1"/></svg>info@tollworthmarks.com</span>
      </div>
      <div class="socials">
        <span class="contact-item"><svg viewBox="0 0 20 20"><circle cx="10" cy="10" r="9" fill="none" stroke="#07080a" stroke-width="1.2"/></svg>@tollworthmarks</span>
        <span class="contact-item"><svg viewBox="0 0 20 20"><circle cx="10" cy="10" r="9" fill="none" stroke="#07080a" stroke-width="1.2"/></svg>@tollworthmarks</span>
      </div>
    </footer>
  </section>

  <section class="card card-front">
    <svg class="chevron" viewBox="0 0 231 132" preserveAspectRatio="none"><polygon points="0,0 39,0 82,66 39,132 0,132" fill="#ee344c"/></svg>
    <div class="brand">
      <span class="brand-square"></span>
      <span class="brand-name">Tollworth Marks</span>
    </div>
  </section>

  <section class="card card-back">
    <svg class="chevron" viewBox="0 0 231 132" preserveAspectRatio="none"><polygon points="0,0 39,0 83,67 39,132 0,132" fill="#ee344c"/></svg>
    <div class="holder">
      <p class="holder-name">DEREK AMSEL</p>
      <p class="holder-role">Solution Maneger</p>
      <ul class="holder-list">
        <li class="contact-item"><svg viewBox="0 0 20 20"><circle cx="10" cy="10" r="9" fill="none" stroke="#ee344c" stroke-width="1.4"/></svg>@tollworthmarks</li>
        <li class="contact-item"><svg viewBox="0 0 20 20"><circle cx="10" cy="10" r="9" fill="none" stroke="#ee344c" stroke-width="1.4"/></svg>@tollworthmarks</li>
        <li class="contact-item"><svg viewBox="0 0 20 20"><circle cx="10" cy="10" r="9" fill="none" stroke="#ee344c" stroke-width="1.4"/><path d="M10 5a3 3 0 0 0-3 3c0 2.5 3 5 3 5s3-2.5 3-5a3 3 0 0 0-3-3z" fill="none" stroke="#fff" stroke-width="1.2"/></svg>Lorem ipsum dolor mirid proud</li>
        <li class="contact-item"><svg viewBox="0 0 20 20"><circle cx="10" cy="10" r="9" fill="none" stroke="#ee344c" stroke-width="1.4"/><path d="M6.5 6.5l2-1 1.2 2.2-1 .9a6 6 0 0 0 2.7 2.7l.9-1 2.2 1.2-1 2C9 13.5 6.5 11 6.5 6.5z" fill="none" stroke="#fff" stroke-width="1.2"/></svg>00 000 0000</li>
        <li class="contact-item"><svg viewBox="0 0 20 20"><circle cx="10" cy="10" r="9" fill="none" stroke="#ee344c" stroke-width="1.4"/><rect x="5.5" y="7" width="9" height="6.5" fill="none" stroke="#fff" stroke-width="1.2"/><path d="M5.5 7l4.5 3.5L14.5 7" fill="none" stroke="#fff" stroke-width="1.2"/></svg>info@tollworthmarks.com</li>
        <li class="contact-item"><svg viewBox="0 0 20 20"><circle cx="10" cy="10" r="9" fill="none" stroke="#ee344c" stroke-width="1.4"/><circle cx="10" cy="10" r="4.5" fill="none" stroke="#fff" stroke-width="1.2"/><path d="M5.5 10h9M10 5.5v9" stroke="#fff" stroke-width="1"/></svg>www.tollworthmarks</li>
      </ul>
    </div>
  </section>

</div>
</body>
</html>
```